Flyer design for webdesign company

create a flyer that can be printed or sent as an email. The flyer needs to be professional, modern and engaging.

Reason: opportunity for all designers to get their designs in.

Target Market(s)

business owners that do not have a website

Industry/Entity Type

It Company

Font styles to use
Sans Serif

```html
<!DOCTYPE html>
<html lang="en">
<head>
<meta charset="utf-8">
<title>nexasites – Website Flyer</title>
<link rel="stylesheet" href="https://fonts.googleapis.com/css2?family=Jost:wght@400;500;600&display=swap">
<style>
  :root {
    --orange: #f6921e;
    --orange-dark: #bc6e1a;
    --ink: #4a4a4a;
    --black: #1c1c1c;
    --white: #ffffff;
    --device-light: #eceff3;
    --device-mid: #cfd1d4;
  }
  * { margin: 0; padding: 0; box-sizing: border-box; }
  html, body { width: 927px; height: 1200px; overflow: hidden; background: var(--white); }
  body { font-family: "Jost", sans-serif; }
  .flyer { position: relative; width: 927px; height: 1200px; overflow: hidden; background: var(--white); }

  .brand { position: absolute; left: 112px; top: 44px; width: 224px; text-align: center; }
  .brand-dot { width: 124px; height: 124px; border-radius: 50%; background: var(--orange); margin: 0 auto 26px; }
  .brand-name { font-size: 32px; font-weight: 500; color: var(--orange); line-height: 1; }

  .hero-band { position: absolute; left: 0; top: 252px; width: 927px; height: 196px; background: var(--orange); }
  .hero-shadow { position: absolute; left: 437px; top: 252px; width: 490px; height: 113px; background: var(--orange-dark); border-radius: 6px 0 0 6px; }

  .contact { position: absolute; left: 40px; top: 270px; color: var(--white); }
  .contact-phone { font-size: 30px; line-height: 40px; }
  .contact-web { font-size: 27px; line-height: 40px; margin-left: 19px; margin-top: 6px; letter-spacing: 0.5px; }

  .device-art { position: absolute; left: 482px; top: 36px; width: 408px; height: 328px; border-radius: 10px;
    background: linear-gradient(180deg, var(--device-light) 0%, var(--device-light) 60%, var(--device-mid) 100%); }
  .offer { position: absolute; left: 498px; top: 56px; width: 376px; height: 210px;
    display: flex; align-items: center; justify-content: center; gap: 8px; }
  .offer-word { font-size: 37px; font-weight: 500; color: var(--black); }
  .offer-price { font-size: 76px; font-weight: 500; color: var(--orange); line-height: 1; position: relative; top: 10px; }
  .offer-price sup { font-size: 42px; vertical-align: 22px; }

  .benefit { position: absolute; top: 388px; width: 320px; text-align: center; }
  .benefit-left { left: 84px; }
  .benefit-right { left: 484px; }
  .benefit-icon { width: 100px; height: 100px; margin: 0 auto; border-radius: 50%; background: var(--white);
    border: 5px solid var(--orange); display: flex; align-items: center; justify-content: center; }
  .benefit-icon svg { width: 62px; height: 50px; }
  .icon-money { font-size: 40px; font-weight: 600; color: var(--orange); letter-spacing: -2px; }
  .benefit-title { margin-top: 14px; font-size: 38px; font-weight: 500; color: var(--orange); line-height: 40px; letter-spacing: 1px; }

  .features { position: absolute; left: 70px; top: 608px; list-style: none; }
  .features li { display: flex; align-items: center; height: 45.6px; font-size: 25.6px; color: var(--ink); }
  .features svg { width: 26px; height: 20px; margin-right: 22px; flex: none; }

  .tagline { position: absolute; left: 76px; top: 950px; font-size: 29px; color: var(--orange); line-height: 40px; letter-spacing: 0.5px; }
  .call-box { position: absolute; left: 524px; top: 954px; width: 356px; height: 78px; border: 4px solid var(--orange);
    display: flex; align-items: center; justify-content: center; font-size: 29px; color: var(--orange); letter-spacing: 1px; }

  .pricing { position: absolute; left: 0; top: 1060px; width: 927px; height: 140px; background: var(--orange);
    color: var(--white); text-align: center; padding-top: 22px; }
  .pricing-main { font-size: 32px; line-height: 40px; letter-spacing: 0.5px; }
  .pricing-note { font-size: 27px; line-height: 40px; margin-top: 4px; }
</style>
</head>
<body>
<main class="flyer">
  <div class="brand">
    <div class="brand-dot"></div>
    <div class="brand-name">nexasites</div>
  </div>

  <div class="hero-band"></div>
  <div class="hero-shadow"></div>

  <div class="contact">
    <p class="contact-phone">Call Today 1-800-555-0142</p>
    <p class="contact-web">www.sitestart247.com</p>
  </div>

  <div class="device-art" role="img" aria-label="Desktop computer monitor showing the daily price offer"></div>
  <div class="offer">
    <span class="offer-word">ONLY</span>
    <span class="offer-price"><sup>$</sup>3</span>
    <span class="offer-word">A DAY</span>
  </div>

  <section class="benefit benefit-left">
    <div class="benefit-icon">
      <svg viewBox="0 0 62 50" role="img" aria-label="Customers icon">
        <circle cx="19" cy="13" r="9" fill="#f6921e"/>
        <circle cx="43" cy="13" r="9" fill="#f6921e"/>
        <path d="M2 48 Q2 26 19 26 Q30 26 33 36 L33 48 Z" fill="#f6921e"/>
        <path d="M29 48 Q29 26 43 26 Q60 26 60 48 Z" fill="#f6921e" stroke="#ffffff" stroke-width="2"/>
      </svg>
    </div>
    <h2 class="benefit-title">ATTRACT MORE<br>CUSTOMERS</h2>
  </section>
  <section class="benefit benefit-right">
    <div class="benefit-icon"><span class="icon-money">$$$</span></div>
    <h2 class="benefit-title">MAKE MORE<br>MONEY</h2>
  </section>

  <ul class="features">
    <li><svg viewBox="0 0 26 20"><path d="M2 10 L10 17 L24 3" fill="none" stroke="#f6921e" stroke-width="4.5"/></svg>97% of people look online for businesses. You need a website</li>
    <li><svg viewBox="0 0 26 20"><path d="M2 10 L10 17 L24 3" fill="none" stroke="#f6921e" stroke-width="4.5"/></svg>You’re losing many customers by not having a website</li>
    <li><svg viewBox="0 0 26 20"><path d="M2 10 L10 17 L24 3" fill="none" stroke="#f6921e" stroke-width="4.5"/></svg>Beat your competition with better visibility and credibility</li>
    <li><svg viewBox="0 0 26 20"><path d="M2 10 L10 17 L24 3" fill="none" stroke="#f6921e" stroke-width="4.5"/></svg>BEAUTIFUL WEBSITES AVAILABLE NOW</li>
    <li><svg viewBox="0 0 26 20"><path d="M2 10 L10 17 L24 3" fill="none" stroke="#f6921e" stroke-width="4.5"/></svg>Smart, clean website designs ($3000 Value. No extra charge)</li>
    <li><svg viewBox="0 0 26 20"><path d="M2 10 L10 17 L24 3" fill="none" stroke="#f6921e" stroke-width="4.5"/></svg>Limited to ONLY 4 WEBSITES per area. Don’t miss out!</li>
    <li><svg viewBox="0 0 26 20"><path d="M2 10 L10 17 L24 3" fill="none" stroke="#f6921e" stroke-width="4.5"/></svg>Social Media setup options (Findly &amp; Friendbook)</li>
  </ul>

  <p class="tagline">Stop wasting money on mailers<br>and print advertising.</p>
  <div class="call-box">CALL 1-800-555-0142</div>

  <footer class="pricing">
    <p class="pricing-main">PRICING: ONLY $99/MONTH &nbsp;(THAT’S $3.30/DAY)</p>
    <p class="pricing-note">(No other costs)</p>
  </footer>
</main>
</body>
</html>
```